Brindle Works Australia Website

Brindle Works Australia (BWA) is a Industrial, Mining & Transport Services provider in Australia. We require a website that is both pc and mobile freindly. The website will be used to both present our company services and give us exposure in a crowded market. The main page of the website will have a snapshot of who BWA is and its from this page that the user can click to enter the area of interest ie. Industrial, Mining and Transport. A disticted logo can be used to indicate the area in question.<br/>Within the industrial, Mining and the Transport services pages will need list and description of services that are provided, current customer lists and news pages.<br/>The website will need a contacts page so prospective customers can get in contact with BWA.<br/>The website design will require a user freindly back end so future updates and ammendments can be carriedout by less experienced people within the BWA business.

Target Market(s)

Industrial, Mining and Transport Services provider markets

Coding

Number of Pages Required

5+ page

Font styles to use
Sans Serif

Colors
00a990

Requirements
Must have
• Ability to build servises with in services. because the main service area is only the main service with in each service group there is alot of smaller services / tasks.
• Key wording for easy seach engine capabilities. The website will need to be search engine freindly.

```html
<!DOCTYPE html>
<html lang="en">
<head>
<meta charset="utf-8">
<title>Brindle Works Australia – Industrial, Mining &amp; Transport Services</title>
<link href="https://fonts.googleapis.com/css2?family=Poppins:wght@400;500;600;700&display=swap" rel="stylesheet">
<style>
:root{
  --green:#07693a;
  --teal:#00a990;
  --ink:#1f1f1f;
  --body:#3d3d3d;
  --muted:#6c6c6c;
  --soft:#f5f6f8;
  --line:#e6e6e6;
  --footer:#231f20;
  --footer-text:#c9c9c9;
}
*{box-sizing:border-box;margin:0;padding:0}
html,body{width:1200px;height:2262px;overflow:hidden}
body{font-family:'Poppins',sans-serif;color:var(--body);background:#fff;position:relative}
.abs{position:absolute}
a{color:inherit;text-decoration:none}

/* header */
.brand{left:234px;top:24px;display:flex;align-items:center;gap:8px}
.brand-mark{width:14px;height:14px;background:var(--green)}
.brand-name{font-size:17px;font-weight:700;color:var(--green);line-height:1.05;width:150px}
.contact-item{top:36px;display:flex;gap:12px;font-size:10px;line-height:16px;color:#333}
.contact-item b{font-weight:500}
.contact-item svg{flex:none;margin-top:2px}

/* nav */
.nav{left:0;top:98px;width:1200px;height:47px;background:var(--green)}
.nav ul{position:absolute;left:234px;top:0;display:flex;list-style:none;height:47px;align-items:center}
.nav li{color:#fff;font-size:8.5px;font-weight:600;margin-right:32px;letter-spacing:.1px}
.nav li.drop::after{content:" ▾";font-size:7px}
.quote{position:absolute;left:823px;top:0;width:143px;height:47px;background:#1d1d1d;clip-path:polygon(14px 0,100% 0,calc(100% - 14px) 100%,0 100%);color:#fff;font-size:10px;font-weight:600;display:flex;align-items:center;justify-content:center}

/* hero */
.hero{left:0;top:145px;width:1200px;height:375px;background:linear-gradient(180deg,#a98262 0%,#c49c74 45%,#b58d66 100%)}
.hero-title{left:0;top:118px;width:1200px;text-align:center;color:#fff;line-height:44px}
.hero-title .light{font-size:38px;font-weight:400;display:block}
.hero-title .bold{font-size:40px;font-weight:700;display:block}
.btn{display:flex;align-items:stretch;height:33px;font-size:11px;font-weight:600;letter-spacing:.2px}
.btn span{display:flex;align-items:center;padding:0 14px}
.btn i{display:flex;align-items:center;justify-content:center;width:27px;border-left:1px solid rgba(255,255,255,.35);font-style:normal}
.btn-teal{background:var(--teal);color:#fff}
.btn-white{background:#fff;color:#222}
.btn-white i{border-left-color:#ddd}
.arrow-circle{top:165px;width:46px;height:46px;border:1.5px solid #fff;border-radius:50%;display:flex;align-items:center;justify-content:center}
.dots{left:570px;top:337px;display:flex;gap:15px}
.dots span{width:10px;height:10px;border:2px solid #fff}
.dots span.on{border-color:var(--teal)}

/* about */
.eyebrow{font-size:9px;font-weight:500;color:var(--teal)}
.about-h{font-size:22px;font-weight:600;line-height:26px;color:#444}
.about-h em{font-style:normal;color:var(--green)}
.about-h b{font-weight:600;color:var(--ink)}
.rule{width:44px;height:2px;background:var(--teal)}
.about-p{font-size:9.2px;line-height:15px;color:#444;width:376px}
.circle{border-radius:50%}

/* services */
.services{left:0;top:889px;width:1200px;height:396px;background:var(--soft)}
.sec-title{width:1200px;left:0;text-align:center;font-size:22px;font-weight:600;color:var(--ink)}
.sec-title em{font-style:normal;color:var(--green)}
.sec-rule{left:577px;width:44px;height:2px;background:var(--teal)}
.card{top:119px;width:232px;height:230px;background:#fff}
.card .num{position:absolute;right:20px;top:12px;font-size:60px;font-weight:700;color:#f0f0f0;line-height:1}
.card .ico{position:absolute;left:22px;top:22px}
.card h3{position:absolute;left:22px;top:97px;font-size:13px;font-weight:600;line-height:19px;color:var(--ink)}
.card p{position:absolute;left:22px;top:138px;width:192px;font-size:10px;line-height:16px;color:#444}
.card .more{position:absolute;left:22px;top:199px;font-size:8px;font-weight:600;color:var(--teal)}

/* news */
.news-card{border:2px solid #ececec;background:#fff}
.meta{display:flex;gap:22px;font-size:9.5px;color:var(--teal)}
.meta span{display:flex;align-items:center;gap:6px}
.news-h{font-size:12.5px;font-weight:600;line-height:19px;color:var(--ink)}
.news-p{font-size:10px;line-height:19px;color:#444}
.read{font-size:10px;font-weight:500;color:var(--green);text-decoration:underline}

/* footer */
.footer{left:0;top:1946px;width:1200px;height:316px;background:var(--footer)}
.f-h{top:60px;font-size:12px;font-weight:600;color:#fff}
.f-rule{top:84px;width:34px;height:2px;background:var(--teal)}
.f-text{font-size:9px;line-height:15px;color:var(--footer-text)}
.links{list-style:none;border-left:1px solid #777;padding-left:15px}
.links li{font-size:9px;color:var(--footer-text);line-height:26.5px;position:relative}
.links li::before{content:"";position:absolute;left:-15px;top:13px;width:8px;height:1px;background:#777}
.social{top:178px;left:234px;display:flex;gap:6px}
.social span{width:27px;height:27px;border:1px solid #888}
.f-contact{display:flex;gap:12px;align-items:center;font-size:9px;color:var(--footer-text);margin-bottom:17px}
.email-box{left:797px;top:143px;width:169px;height:37px;background:#4a4647;display:flex;align-items:center;justify-content:space-between;padding:0 14px;font-size:9px;color:#cfcfcf}
.f-bottom{left:234px;top:250px;width:731px;border-top:1px solid #3c3839}
.copy{left:234px;top:284px;font-size:9px;color:var(--footer-text)}
.legal{right:234px;top:284px;display:flex;gap:12px;align-items:center;font-size:9px;color:var(--footer-text)}
.legal i{width:4px;height:4px;border-radius:50%;background:#666}
</style>
</head>
<body>

<header>
  <div class="abs brand">
    <span class="brand-mark"></span>
    <span class="brand-name">Brindle Works Australia</span>
  </div>
  <div class="abs contact-item" style="left:501px">
    <svg width="13" height="19" viewBox="0 0 13 19"><path d="M6.5 0A6.5 6.5 0 0 0 0 6.5C0 11 6.5 19 6.5 19S13 11 13 6.5A6.5 6.5 0 0 0 6.5 0z" fill="#07693a"/><circle cx="6.5" cy="6.5" r="2.4" fill="#fff"/></svg>
    <div>PO Box 1425<br>Harlow WA 6917</div>
  </div>
  <div class="abs contact-item" style="left:642px">
    <svg width="19" height="19" viewBox="0 0 24 24"><path d="M6.6 10.8a15.1 15.1 0 0 0 6.6 6.6l2.2-2.2a1 1 0 0 1 1-.25 11.4 11.4 0 0 0 3.6.57 1 1 0 0 1 1 1V20a1 1 0 0 1-1 1A17 17 0 0 1 3 4a1 1 0 0 1 1-1h3.5a1 1 0 0 1 1 1c0 1.25.2 2.45.57 3.57a1 1 0 0 1-.25 1z" fill="#07693a"/></svg>
    <div><b>Phone</b><br>+61 (0)400 118 905</div>
  </div>
  <div class="abs contact-item" style="left:790px">
    <svg width="20" height="20" viewBox="0 0 20 20"><rect width="20" height="20" fill="#07693a"/><path d="M3 4l14 12M17 4L3 16" stroke="#fff" stroke-width="1.6"/></svg>
    <div><b>Email</b><br>hello@brindleworks.example</div>
  </div>
</header>

<nav class="abs nav">
  <ul>
    <li>HOME</li><li>ABOUT US</li><li class="drop">SERVICES</li><li class="drop">PROJECT</li><li>CUSTOMER LIST</li><li>NEWS</li><li>CONTACT US</li>
  </ul>
  <div class="quote">GET A QUOTE</div>
</nav>

<section class="abs hero" role="img" aria-label="Excavator and bulldozer working in a sandy open-cut quarry">
  <h1 class="abs hero-title"><span class="light">We Provide Best</span><span class="bold">Industrial Services</span></h1>
  <div class="abs" style="left:463px;top:224px;display:flex;gap:14px">
    <a class="btn btn-teal"><span>OUR SERVICES</span><i>›</i></a>
    <a class="btn btn-white"><span style="font-weight:500">CONTACT US</span><i>›</i></a>
  </div>
  <div class="abs arrow-circle" style="left:125px"><svg width="10" height="14" viewBox="0 0 10 14"><path d="M8 1L2 7l6 6" stroke="#fff" stroke-width="1.6" fill="none"/></svg></div>
  <div class="abs arrow-circle" style="left:1028px"><svg width="10" height="14" viewBox="0 0 10 14"><path d="M2 1l6 6-6 6" stroke="#fff" stroke-width="1.6" fill="none"/></svg></div>
  <div class="abs dots"><span class="on"></span><span></span><span></span></div>
</section>

<section class="about">
  <div class="abs eyebrow" style="left:234px;top:575px">ABOUT US</div>
  <h2 class="abs about-h" style="left:234px;top:594px">Welcome to<br><em>Brindle</em> <b>Works</b> <em>Australia</em></h2>
  <div class="abs rule" style="left:234px;top:656px"></div>
  <p class="abs about-p" style="left:233px;top:677px">Lorem ipsum dolor sit amet, consectetur adipiscing elit. Fusce luctus imperdiet nisl, viverra efficitur massa egestas ac. Ut imperdiet ut turpis nec efficitur. Sed interdum nisl quis nulla elementum, rutrum elementum sapien convallis. Aenean sed feugiat ligula. Mauris rutrum iaculis turpis in aliquet. Aenean tempor mi lacus, sit amet porttitor felis interdum id. Proin non ipsum tellus. Morbi ullamcorper tortor ac aliquet sagittis. Nulla id purus eget velit suscipit pretium. Aliquam auctor tortor quis elit bibendum, sed laoreet justo sodales.</p>
  <a class="abs btn btn-teal" style="left:234px;top:801px;height:33px"><span>READ MORE</span><i>›</i></a>
  <div class="abs circle" style="left:647px;top:595px;width:220px;height:220px;background:linear-gradient(160deg,#9a9a96,#6d6256 55%,#3d3a34)" role="img" aria-label="Haul truck loaded at a rocky mine site"></div>
  <div class="abs circle" style="left:809px;top:682px;width:132px;height:132px;background:radial-gradient(circle at 45% 40%,#3d9f8c,#1d7a68);border:3px solid #fff;display:flex;align-items:center;justify-content:center" role="img" aria-label="Video preview of mining machinery">
    <svg width="38" height="38" viewBox="0 0 38 38"><circle cx="19" cy="19" r="17.5" stroke="#fff" stroke-width="1.5" fill="none"/><path d="M15 12l11 7-11 7z" fill="#fff"/></svg>
  </div>
</section>

<section class="abs services">
  <h2 class="abs sec-title" style="top:35px">Our <em>Services</em></h2>
  <div class="abs sec-rule" style="top:77px"></div>

  <article class="abs card" style="left:234px">
    <div class="num">01</div>
    <svg class="ico" width="62" height="58" viewBox="0 0 62 58"><path d="M0 58V30l14-8v8l14-8v8l14-8V10h8v48z" fill="#07693a"/><rect x="6" y="40" width="8" height="5" fill="#fff"/><rect x="18" y="40" width="8" height="5" fill="#fff"/><rect x="30" y="40" width="8" height="5" fill="#fff"/><rect x="6" y="49" width="8" height="5" fill="#fff"/><rect x="18" y="49" width="8" height="5" fill="#fff"/><rect x="30" y="49" width="8" height="5" fill="#fff"/><circle cx="50" cy="6" r="6" fill="#07693a"/><circle cx="58" cy="5" r="4" fill="#07693a"/></svg>
    <h3>BWA Industrial Services<br>Division</h3>
    <p>BWA Industrial Services Division offers an integrated site service and maintenance of your fixed plant.</p>
    <a class="more">READ MORE &nbsp;›</a>
  </article>

  <article class="abs card" style="left:484px">
    <div class="num">02</div>
    <svg class="ico" width="84" height="50" viewBox="0 0 84 50"><rect x="12" y="4" width="20" height="18" fill="#07693a"/><rect x="16" y="8" width="12" height="9" fill="#fff"/><path d="M6 22h46l8 8v6H6z" fill="#07693a"/><rect x="0" y="34" width="60" height="14" rx="7" fill="#07693a"/><circle cx="10" cy="41" r="3" fill="#fff"/><circle cx="22" cy="41" r="3" fill="#fff"/><circle cx="34" cy="41" r="3" fill="#fff"/><circle cx="46" cy="41" r="3" fill="#fff"/><path d="M60 30l12 0 12 18H66z" fill="#07693a"/></svg>
    <h3>BWA Mining Services<br>Division</h3>
    <p>BWA Mining Services Division offers an integrated service in equipment rental, maintenance and earthmoving.</p>
    <a class="more">READ MORE &nbsp;›</a>
  </article>

  <article class="abs card" style="left:734px">
    <div class="num">03</div>
    <svg class="ico" width="78" height="58" viewBox="0 0 78 58"><path d="M36 0h26v40H36z" fill="#07693a"/><path d="M16 10h18v30H2V26z" fill="#07693a"/><rect x="18" y="14" width="10" height="9" fill="#fff"/><rect x="0" y="40" width="78" height="8" fill="#07693a"/><circle cx="14" cy="50" r="7" fill="#07693a" stroke="#fff" stroke-width="2"/><circle cx="48" cy="50" r="7" fill="#07693a" stroke="#fff" stroke-width="2"/><circle cx="64" cy="50" r="7" fill="#07693a" stroke="#fff" stroke-width="2"/></svg>
    <h3>BWA Transport<br>Division</h3>
    <p>BWA Transport Division specialises in the transportation of all types of materials such as, Steel, Structural Steel..</p>
    <a class="more">READ MORE &nbsp;›</a>
  </article>
</section>

<section class="news">
  <h2 class="abs sec-title" style="top:1330px">Latest <em>News</em></h2>
  <div class="abs sec-rule" style="top:1372px"></div>

  <article class="abs news-card" style="left:234px;top:1412px;width:419px;height:476px">
    <div style="height:227px;margin:-2px -2px 0;background:linear-gradient(180deg,#1d2450 0%,#2a2f5e 55%,#7a4a3a 85%,#c7743a 100%)" role="img" aria-label="Industrial power plant with chimneys at night"></div>
    <div class="abs meta" style="left:32px;top:255px">
      <span><svg width="12" height="12" viewBox="0 0 12 12"><rect x=".5" y="1.5" width="11" height="10" fill="none" stroke="#00a990"/><path d="M.5 4.5h11M3 0v3M9 0v3" stroke="#00a990"/></svg>4th January 2019</span>
      <span><svg width="15" height="12" viewBox="0 0 15 12"><path d="M1 1h9v6H5l-3 2V7H1z M11 4h3v5h-1v2l-2-2H7" fill="none" stroke="#00a990"/></svg>43 Comments</span>
    </div>
    <h3 class="abs news-h" style="left:32px;top:285px;width:360px">Lorem ipsum dolor sit amet, consectetur adipiscing elit. Fusce luctus imperdiet nisl viverra efficitur massa.</h3>
    <p class="abs news-p" style="left:32px;top:346px;width:362px">Lorem ipsum dolor sit amet, consectetur adipiscing elit. Fusce luctus imperdiet nisl, viverra efficitur massa egestas ac. Ut imperdiet ut turpis nec efficitur. Sed interdum nisl quis nulla elementum, rutrum elementum sapien convallis.</p>
    <a class="abs read" style="left:32px;top:430px">Read More</a>
  </article>

  <article class="abs news-card" style="left:673px;top:1412px;width:292px;height:145px">
    <div class="abs meta" style="left:26px;top:29px">
      <span><svg width="12" height="12" viewBox="0 0 12 12"><rect x=".5" y="1.5" width="11" height="10" fill="none" stroke="#00a990"/><path d="M.5 4.5h11M3 0v3M9 0v3" stroke="#00a990"/></svg>4th January 2019</span>
      <span><svg width="15" height="12" viewBox="0 0 15 12"><path d="M1 1h9v6H5l-3 2V7H1z M11 4h3v5h-1v2l-2-2H7" fill="none" stroke="#00a990"/></svg>43 Comments</span>
    </div>
    <h3 class="abs news-h" style="left:26px;top:59px;width:245px">Nunc id mollis nunc, sit amet tincid­unt est. Vivamus ut metus rhoncus, dictum est eget, faucibus nunc.</h3>
  </article>

  <article class="abs news-card" style="left:673px;top:1577px;width:292px;height:145px">
    <div class="abs meta" style="left:26px;top:29px">
      <span><svg width="12" height="12" viewBox="0 0 12 12"><rect x=".5" y="1.5" width="11" height="10" fill="none" stroke="#00a990"/><path d="M.5 4.5h11M3 0v3M9 0v3" stroke="#00a990"/></svg>4th January 2019</span>
      <span><svg width="15" height="12" viewBox="0 0 15 12"><path d="M1 1h9v6H5l-3 2V7H1z M11 4h3v5h-1v2l-2-2H7" fill="none" stroke="#00a990"/></svg>43 Comments</span>
    </div>
    <h3 class="abs news-h" style="left:26px;top:59px;width:225px">Vestibulum ante ipsum primis in faucibus orci luctus et ultrices posuere cubilia Curae</h3>
  </article>

  <article class="abs news-card" style="left:673px;top:1744px;width:292px;height:145px">
    <div class="abs meta" style="left:26px;top:29px">
      <span><svg width="12" height="12" viewBox="0 0 12 12"><rect x=".5" y="1.5" width="11" height="10" fill="none" stroke="#00a990"/><path d="M.5 4.5h11M3 0v3M9 0v3" stroke="#00a990"/></svg>4th January 2019</span>
      <span><svg width="15" height="12" viewBox="0 0 15 12"><path d="M1 1h9v6H5l-3 2V7H1z M11 4h3v5h-1v2l-2-2H7" fill="none" stroke="#00a990"/></svg>43 Comments</span>
    </div>
    <h3 class="abs news-h" style="left:26px;top:59px;width:245px">Donec varius iaculis nibh eget molestie. Curabitur at libero dictum, egestas magna nec,</h3>
  </article>
</section>

<footer class="abs footer">
  <h4 class="abs f-h" style="left:234px">ABOUT US</h4>
  <div class="abs f-rule" style="left:234px"></div>
  <p class="abs f-text" style="left:234px;top:106px;width:170px">Lorem ipsum dolor sit amet, consectetur adipiscing elit. Fusce luctus imperdiet nisl, viverra efficitur massa egestas ac.</p>
  <div class="abs social"><span></span><span></span><span></span><span></span></div>

  <h4 class="abs f-h" style="left:421px">QUICK LINKS</h4>
  <div class="abs f-rule" style="left:421px"></div>
  <ul class="abs links" style="left:426px;top:100px"><li>Home</li><li>About Us</li><li>Services</li><li>Projects</li></ul>
  <ul class="abs links" style="left:507px;top:100px;height:80px"><li>Customer List</li><li>News</li><li>Contact Us</li></ul>

  <h4 class="abs f-h" style="left:610px">CONTACT INFO</h4>
  <div class="abs f-rule" style="left:610px"></div>
  <div class="abs" style="left:610px;top:103px">
    <div class="f-contact"><svg width="9" height="13" viewBox="0 0 13 19"><path d="M6.5 0A6.5 6.5 0 0 0 0 6.5C0 11 6.5 19 6.5 19S13 11 13 6.5A6.5 6.5 0 0 0 6.5 0z" fill="#00a990"/><circle cx="6.5" cy="6.5" r="2.4" fill="#231f20"/></svg>PO Box 1425 Harlow WA 6917</div>
    <div class="f-contact"><svg width="9" height="13" viewBox="0 0 9 13"><rect x=".75" y=".75" width="7.5" height="11.5" rx="1" fill="none" stroke="#00a990" stroke-width="1.5"/><circle cx="4.5" cy="10" r=".9" fill="#00a990"/></svg>+61 (0)400 118 905</div>
    <div class="f-contact"><svg width="12" height="9" viewBox="0 0 12 9"><rect x=".5" y=".5" width="11" height="8" fill="none" stroke="#00a990"/><path d="M.5 .5L6 5l5.5-4.5" fill="none" stroke="#00a990"/></svg>hello@brindleworks.example</div>
  </div>

  <h4 class="abs f-h" style="left:797px">NEWSLETTER</h4>
  <div class="abs f-rule" style="left:797px"></div>
  <p class="abs f-text" style="left:797px;top:106px;width:170px">You will be notified when somthing new will be appear.</p>
  <div class="abs email-box">Email Address*<svg width="15" height="11" viewBox="0 0 15 11"><rect x=".75" y=".75" width="13.5" height="9.5" fill="none" stroke="#fff" stroke-width="1.2"/><path d="M.75 .75L7.5 6l6.75-5.25" fill="none" stroke="#fff" stroke-width="1.2"/></svg></div>

  <div class="abs f-bottom"></div>
  <p class="abs copy">Copyright © 2019 Brindle Works Australia. All rights reserved.</p>
  <div class="abs legal"><span>Privacy</span><i></i><span>Terms of Use</span><i></i><span>Cookies</span></div>
</footer>

</body>
</html>
```